High end Electrical/home automation Business Card

Need a card for a high end electrical and home automation company utilising the existing logo.
Phone
Email
Website

Like black look with raised detail. Don’t necessarily need to keep colour of logo it could be made grayscale or white etc

Target Market(s)

High end clients

Contact Information for Business Card

Northwell Electrical

Requirements
Must have
• Logo, phone, email, website, address

High end look
Nice to have
• Black background card
Raised font
Should not have
• Lots of colour

```html
<!DOCTYPE html>
<html lang="en">
<head>
<meta charset="utf-8">
<title>Northwell Electrical – Business Card</title>
<link rel="stylesheet" href="https://fonts.googleapis.com/css2?family=Open+Sans:ital,wght@0,400;0,700;1,400&display=swap">
<style>
  :root {
    --backdrop: #c4c5c1;
    --card: #2f2f2f;
    --text-light: #f2f2f2;
    --accent: #1e8fd0;
    --emboss: #363636;
    --emboss-edge: #3c3c3c;
  }
  * { margin: 0; padding: 0; box-sizing: border-box; }
  html, body {
    width: 1200px;
    height: 884px;
    overflow: hidden;
    background: var(--backdrop);
  }
  .canvas {
    position: relative;
    width: 1200px;
    height: 884px;
    display: flex;
    align-items: center;
    justify-content: center;
  }
  .card {
    position: relative;
    width: 1000px;
    height: 572px;
    background: var(--card);
    font-family: "Open Sans", sans-serif;
    color: var(--text-light);
    overflow: hidden;
  }
  .emboss-mark {
    position: absolute;
    left: 560px;
    top: 90px;
    width: 400px;
    height: 420px;
    border-radius: 50%;
    background: radial-gradient(circle at 45% 40%, var(--emboss-edge), var(--emboss) 70%);
  }
  .brand-name {
    position: absolute;
    left: 78px;
    top: 46px;
    font-size: 44px;
    font-weight: 700;
    letter-spacing: -0.5px;
    color: var(--text-light);
  }
  .contact-person {
    position: absolute;
    left: 96px;
    top: 148px;
  }
  .person-name {
    font-size: 30px;
    font-weight: 700;
    color: var(--accent);
    line-height: 1.1;
  }
  .person-role {
    font-size: 21px;
    font-style: italic;
    line-height: 1.3;
  }
  .address {
    position: absolute;
    left: 96px;
    top: 246px;
    font-size: 22px;
    line-height: 1.3;
    font-style: italic;
  }
  .contact-list {
    position: absolute;
    left: 70px;
    top: 330px;
    list-style: none;
    font-size: 22px;
    line-height: 1.45;
    font-style: italic;
  }
  .contact-list li {
    display: flex;
    align-items: center;
    gap: 10px;
  }
  .contact-icon {
    width: 18px;
    height: 18px;
    flex: none;
  }
</style>
</head>
<body>
<div class="canvas">
  <section class="card">
    <div class="emboss-mark" role="img" aria-label="Large embossed brand mark, tone on tone"></div>

    <div class="brand-name">Northwell Electrical</div>

    <div class="contact-person">
      <div class="person-name">Daniel Harper</div>
      <div class="person-role">President</div>
    </div>

    <address class="address">
      27 Marlow Street<br>
      Coral Bay, Florida 33190
    </address>

    <ul class="contact-list">
      <li>
        <svg class="contact-icon" viewBox="0 0 24 24" aria-hidden="true">
          <path fill="#1e8fd0" d="M6.6 10.8a15.1 15.1 0 0 0 6.6 6.6l2.2-2.2a1 1 0 0 1 1-.25 11.4 11.4 0 0 0 3.6.57 1 1 0 0 1 1 1V20a1 1 0 0 1-1 1A17 17 0 0 1 3 4a1 1 0 0 1 1-1h3.5a1 1 0 0 1 1 1c0 1.25.2 2.46.57 3.6a1 1 0 0 1-.25 1z"/>
        </svg>
        (123) 555-0187
      </li>
      <li>
        <svg class="contact-icon" viewBox="0 0 24 24" aria-hidden="true">
          <rect x="2" y="5" width="20" height="14" fill="none" stroke="#1e8fd0" stroke-width="2"/>
          <path d="M2 5l10 8 10-8" fill="none" stroke="#1e8fd0" stroke-width="2"/>
        </svg>
        daniel@northwellelectrical.co.nz
      </li>
      <li>
        <svg class="contact-icon" viewBox="0 0 24 24" aria-hidden="true">
          <g fill="none" stroke="#1e8fd0" stroke-width="1.8">
            <circle cx="12" cy="12" r="10"/>
            <ellipse cx="12" cy="12" rx="4.5" ry="10"/>
            <path d="M2 12h20M4 7h16M4 17h16"/>
          </g>
        </svg>
        www.northwellelectrical.co.nz
      </li>
    </ul>
  </section>
</div>
</body>
</html>
```